I have a requirement for a simple website that I can manage and change content myself. I'd like to be able to include and change images frequently.

I run a small consulting firm and focus on the area of small to medium sized business turn around. The premise of the business service is that most small businesses "have a monkey on their back" - a problem they need to solve - for example "a Sales Monkey" where their sales team didn't have a solid process or approach or training or the right people; or "a Finance Monkey" where they needed help with Cash flow management or funding, or "an IT Monkey" where their IT systems aren't supporting their supply chain process or ordering process.

So the whole business is build around building monkey characters to represent specific business problems - thus the name Quiet Harbour Partners.

This always builds into giving each employee their own Monkey character - mine is an Orangutan and appears on my card and Derek (who is our Lawyer) is a Baboon and his character is on his card. I'd like to see these characters also integrated into the site.

The site need to be pretty simple at this stage:

1. Home Page
2. Services Page
3. Who we are / team page
4. Contact Us page

Due to the nature of the name and the imagery around the business I'd like the site to be engaging and colourful, the language I'll use is accessible, down to earth and customer/solution focused.

Target Market(s)

Small to medium sized enterprises looking for assistance with their business. They will be looking for practical solutions at value for money pricing

Industry/Entity Type

Business Service

Requirements
Nice to have
• I'd like the monkey in the logo to swing.

On the People or team page - each person is to have their own monkey character - for example - my business card shows my monkey character as an Orangutan and Derek's monkey character is a baboon - so as the business grows each new person gets their own monkeys character. So on the people or team page it would be fun to have some kind of jungle scene with the character monkeys placed in there and some descriptor of the person.

```html
<!DOCTYPE html>
<html lang="en">
<head>
<meta charset="utf-8">
<title>Quiet Harbour Partners – Main Jungle</title>
<link rel="stylesheet" href="https://fonts.googleapis.com/css2?family=Quicksand:wght@400;500;600&family=Noto+Sans:wght@400&display=swap">
<style>
  :root {
    --jungle-deep: #0a5a1c;
    --jungle-mid: #2f8f1e;
    --jungle-light: #6cbf2a;
    --panel-brown: #7a4300;
    --panel-edge: #c9b800;
    --panel-edge-dark: #9a8600;
    --gold: #dcc24e;
    --gold-soft: #ccb46e;
    --gold-bright: #e6d200;
    --nav-orange: #f0a23a;
    --nav-orange-light: #f8c068;
    --nav-orange-dark: #c87818;
    --nav-text: #6a3a08;
    --frame-gold: #c8b400;
    --frame-inner: #6e5a00;
  }
  html, body {
    margin: 0;
    padding: 0;
    width: 1200px;
    height: 1020px;
    overflow: hidden;
  }
  .canvas {
    position: relative;
    width: 1200px;
    height: 1020px;
    overflow: hidden;
    font-family: "Quicksand", sans-serif;
  }
  .jungle-backdrop {
    position: absolute;
    inset: 0;
    background: linear-gradient(115deg, var(--jungle-deep) 0%, var(--jungle-mid) 35%, var(--jungle-light) 55%, var(--jungle-mid) 75%, var(--jungle-deep) 100%);
  }
  .page-panel {
    position: absolute;
    left: 146px;
    top: 12px;
    width: 910px;
    height: 994px;
    box-sizing: border-box;
    background: var(--panel-brown);
    border-left: 6px solid var(--panel-edge);
    border-right: 6px solid var(--panel-edge);
    border-top: 3px solid var(--panel-edge-dark);
    border-bottom: 3px solid var(--panel-edge-dark);
    border-radius: 20px;
  }
  .brand-name {
    position: absolute;
    left: 210px;
    top: 40px;
    margin: 0;
    font-family: "Quicksand", sans-serif;
    font-weight: 500;
    font-size: 44px;
    letter-spacing: 1px;
    color: var(--gold-bright);
    line-height: 1;
  }
  .main-nav {
    position: absolute;
    left: 220px;
    top: 139px;
    width: 761px;
    height: 46px;
    box-sizing: border-box;
    border-top: 3px solid var(--nav-orange-light);
    border-bottom: 3px solid var(--nav-orange-light);
    background: linear-gradient(180deg, var(--nav-orange-light) 0%, var(--nav-orange) 40%, var(--nav-orange-dark) 100%);
    display: flex;
    align-items: center;
    padding-left: 2px;
  }
  .nav-item {
    display: flex;
    align-items: center;
    height: 36px;
    font-family: "Noto Sans", sans-serif;
    font-size: 12px;
    color: var(--nav-text);
    border-right: 1px solid var(--nav-orange-dark);
  }
  .nav-label {
    display: flex;
    align-items: center;
    justify-content: center;
    height: 100%;
    padding: 0 8px;
  }
  .nav-item.is-active .nav-label {
    border: 1px solid var(--nav-orange-dark);
    height: 28px;
    background: linear-gradient(180deg, var(--nav-orange-light), var(--nav-orange));
    box-sizing: border-box;
  }
  .nav-mascot {
    width: 20px;
    height: 30px;
    margin: 0 28px;
    border-radius: 8px 8px 3px 3px;
    background: linear-gradient(180deg, #5a5a5a, #2a2a2a);
  }
  .nav-item:nth-child(1) .nav-label { width: 104px; }
  .nav-item:nth-child(2) .nav-label { width: 80px; }
  .nav-item:nth-child(3) .nav-label { width: 70px; }
  .nav-item:nth-child(4) { border-right: none; }
  .nav-item:nth-child(4) .nav-label { width: 110px; padding-left: 18px; }
  .hero-text {
    position: absolute;
    left: 198px;
    top: 263px;
    width: 605px;
    margin: 0;
    font-size: 21px;
    line-height: 26.8px;
    font-weight: 500;
    color: var(--gold);
    letter-spacing: -0.3px;
  }
  .hero-figure {
    position: absolute;
    left: 798px;
    top: 213px;
    width: 278px;
    height: 363px;
    border-radius: 120px 110px 30px 40px;
    background: radial-gradient(ellipse at 40% 35%, #e8d400 0%, #d4c000 55%, #a88a00 100%);
  }
  .section-heading {
    margin: 0;
    font-size: 18px;
    font-weight: 400;
    color: var(--gold-soft);
    line-height: 22px;
  }
  .gallery {
    position: absolute;
    left: 198px;
    top: 610px;
    width: 300px;
  }
  .photo-frame {
    position: absolute;
    box-sizing: border-box;
    border: 5px solid var(--frame-gold);
    box-shadow: inset 0 0 0 2px var(--frame-inner);
    padding: 4px;
  }
  .photo-frame .photo {
    width: 100%;
    height: 100%;
  }
  .photo-frame.is-orangutan { left: 0; top: 66px; width: 81px; height: 170px; }
  .photo-frame.is-orangutan .photo { background: linear-gradient(180deg, #8a5a10, #f06a28 30%, #e85a20); }
  .photo-frame.is-baboon { left: 85px; top: 110px; width: 88px; height: 126px; }
  .photo-frame.is-baboon .photo { background: linear-gradient(180deg, #6a6a6a, #303030 70%, #3e8a1e); }
  .about-block {
    position: absolute;
    left: 524px;
    top: 611px;
    width: 460px;
  }
  .about-block p,
  .contact-block p {
    margin: 0;
    font-size: 14px;
    line-height: 18px;
    color: var(--gold);
  }
  .about-block p {
    margin: 16px 0 0 18px;
    width: 440px;
  }
  .contact-block {
    position: absolute;
    left: 524px;
    top: 783px;
    width: 330px;
  }
  .contact-block p {
    margin: 18px 0 0 18px;
    width: 310px;
  }
  .contact-block strong { font-weight: 600; }
  .footer-rule {
    position: absolute;
    left: 198px;
    top: 932px;
    width: 804px;
    height: 5px;
    background: linear-gradient(180deg, var(--gold-bright), var(--panel-edge-dark));
  }
  .site-footer {
    position: absolute;
    left: 146px;
    width: 910px;
    top: 965px;
    text-align: center;
    font-size: 14px;
    color: var(--gold);
  }
</style>
</head>
<body>
<div class="canvas">
  <div class="jungle-backdrop" role="img" aria-label="Green jungle leaves background with playful monkey line drawings"></div>

  <div class="page-panel"></div>

  <h1 class="brand-name">quiet harbour partners</h1>

  <nav class="main-nav">
    <div class="nav-item is-active"><span class="nav-label">Main Jungle</span><span class="nav-mascot" role="img" aria-label="Small gorilla icon"></span></div>
    <div class="nav-item"><span class="nav-label">The Primates</span><span class="nav-mascot" role="img" aria-label="Small gorilla icon"></span></div>
    <div class="nav-item"><span class="nav-label">Contact Us</span><span class="nav-mascot" role="img" aria-label="Small gorilla icon"></span></div>
    <div class="nav-item"><span class="nav-label">Jungle Services</span><span class="nav-mascot" role="img" aria-label="Small gorilla icon"></span></div>
  </nav>

  <p class="hero-text">(what ever you want main focus of this page will go here) example text: The premise of the business service is that most small businesses "have a monkey on their back" - a problem they need to solve - for example "a Sales Monkey" where their sales team didn't have a solid process or approach or training or the right people; or "a Finance Monkey" where they needed help with Cash flow management or funding, or "an IT Monkey" where their IT systems aren't supporting their supply chain process or ordering process.</p>

  <div class="hero-figure" role="img" aria-label="Large yellow gorilla illustration standing on all fours"></div>

  <section class="gallery">
    <h2 class="section-heading">Image Holders (the image border and frames will adjust to your picture size)</h2>
    <div class="photo-frame is-orangutan"><div class="photo" role="img" aria-label="Orange orangutan character hanging from a branch"></div></div>
    <div class="photo-frame is-baboon"><div class="photo" role="img" aria-label="Grey gorilla character sitting in grass"></div></div>
  </section>

  <section class="about-block">
    <h2 class="section-heading">Inside the Jungle</h2>
    <p>A brief discription about how your company was startd or founded (Lorem Ipsum Dolor Sit Amet, Consectetuer Adipiscing Elit. Nam Cursus. Morbi Ut Mi. Nullam Enim Leo, Egestas Id, Condimentum At, Laoreet Mattis, Massa. Sed Eleifend Nonummy Diam. Praesent Mauris Ante, Elementum Et, Bibendum At, Posuere Sit Amet, Nibh.)</p>
  </section>

  <section class="contact-block">
    <h2 class="section-heading">Contact The Jungle</h2>
    <p>Call us: <strong>1-800-Your-Number</strong><br>
    Email us: address@youremailaddres<br>
    If you are on Chatterbook, tweetly, linkwork I can create custom follow us buttons for you as well in a jungle theme</p>
  </section>

  <div class="footer-rule"></div>
  <footer class="site-footer">© 2013 Quiet Harbour Partners. All Rights Reserved.</footer>
</div>
</body>
</html>
```